Hale Accounting firm needing a captivating business card

We need a business card design that forces the person to look at the card because its either gold foil, plastic, or lettering pop up etc. We already have a logo with a specific gold color and we need to make it pop. We are an accounting firm. I need the words" accounting, payroll, licenses, audits, taxes" somewhere on the business card so as to describe what we do- preferably on the side where the logo is at.

Industry/Entity Type

Accounting

Contact Information for Business Card

Address 48276 9th Ave S Ste 305, Federal Way, WA 98117
Business Phone (360)418-2096
Fax (360)418-2157
Office Cell Phone (360)586-7319

Font styles to use
Serif

Colors
85abd2

Requirements
Must have
• It should state
• "Accounting" "Taxes" "Audits" "Licenses" "Payroll"
Nice to have
• Matte with gold foil, different textures, With Either a textured ivory background or gray blue slate background
Should not have
• colorful colors

```html
<!DOCTYPE html>
<html lang="en">
<head>
<meta charset="utf-8">
<title>Hale Accounting — Business Card</title>
<link href="https://fonts.googleapis.com/css2?family=Bebas+Neue&family=Oswald:wght@300;400&display=swap" rel="stylesheet">
<style>
  :root {
    --stage: #0b0e1a;
    --card: #1e2028;
    --band: #141518;
    --panel: #26262c;
    --rule: #4a4b52;
    --gold: #f2c25a;
    --gold-deep: #d89a25;
    --gold-soft: #e8cf9e;
  }
  * { margin: 0; padding: 0; box-sizing: border-box; }
  html, body { width: 1200px; height: 906px; overflow: hidden; background: var(--stage); }
  .stage { position: relative; width: 1200px; height: 906px; background: var(--stage); }

  .card {
    position: absolute;
    border-radius: 16px;
    background: var(--card);
    box-shadow: 0 10px 40px rgba(0,0,0,.55);
    overflow: hidden;
  }
  .card--front { left: 148px; top: 71px; width: 434px; height: 761px; }
  .card--back  { left: 641px; top: 69px; width: 436px; height: 763px; }

  .band {
    position: absolute; left: 0; width: 100%;
    background: var(--band);
    box-shadow: 0 3px 6px rgba(0,0,0,.5), 0 -1px 0 rgba(0,0,0,.6);
  }
  .band--brand { top: 35px; height: 186px; }
  .band--heading { top: 258px; height: 91px; display: flex; align-items: center; justify-content: center; }

  .brand { position: absolute; left: 0; top: 0; width: 100%; height: 100%; display: flex; flex-direction: column; align-items: center; justify-content: center; gap: 14px; }
  .brand__mark { width: 46px; height: 46px; border-radius: 50%; background: linear-gradient(135deg, var(--gold), var(--gold-deep)); }
  .brand__name { font-family: "Bebas Neue", sans-serif; font-size: 38px; color: var(--gold); letter-spacing: 1px; line-height: 1; }

  .tagline {
    position: absolute; left: 0; top: 262px; width: 100%; text-align: center;
    font-family: "Oswald", sans-serif; font-weight: 400; font-size: 20px;
    letter-spacing: 4.5px; color: var(--gold-soft);
  }

  .contact {
    position: absolute; left: 33px; width: 369px; height: 84px;
    background: var(--panel); border-radius: 3px;
    box-shadow: 0 2px 4px rgba(0,0,0,.5);
    display: flex; flex-direction: column; justify-content: center;
    padding-left: 27px;
    font-family: "Bebas Neue", sans-serif; font-size: 21px; line-height: 26px;
    color: var(--gold);
  }
  .contact--address { top: 334px; }
  .contact--phone { top: 439px; }
  .contact--fax { top: 545px; }
  .contact--email { top: 652px; }

  .seal { position: absolute; left: 119px; top: 26px; }

  .section-title {
    font-family: "Oswald", sans-serif; font-weight: 300; font-size: 23px;
    letter-spacing: 10px; color: var(--gold-soft);
  }

  .services { list-style: none; }
  .service {
    position: absolute; left: 0; width: 100%;
    font-family: "Bebas Neue", sans-serif; font-size: 25px; color: var(--gold);
  }
  .service__arrow { position: absolute; left: 13px; top: 5px; width: 18px; height: 20px; }
  .service__label { position: absolute; left: 55px; top: 0; line-height: 30px; }
  .rule { position: absolute; left: 49px; width: 359px; height: 2px; background: var(--rule); }

  .firm-name {
    position: absolute; left: 0; top: 720px; width: 100%; text-align: center;
    font-family: "Bebas Neue", sans-serif; font-size: 18px; letter-spacing: 14px;
    color: var(--gold-soft); padding-left: 14px;
  }

  .card-label {
    position: absolute; top: 854px; width: 440px; text-align: center;
    font-family: "Bebas Neue", sans-serif; font-size: 21px; letter-spacing: 12px;
    color: var(--gold);
  }
  .card-label--front { left: 145px; }
  .card-label--back { left: 639px; }
</style>
</head>
<body>
<main class="stage">

  <section class="card card--front" aria-label="Front of card">
    <div class="band band--brand">
      <div class="brand">
        <span class="brand__mark" aria-hidden="true"></span>
        <span class="brand__name">HALE</span>
      </div>
    </div>
    <p class="tagline">THERE IS NO MISCALCULATION</p>
    <div class="contact contact--address">
      <span>ADDRESS 48276 9TH AVE S STE 305,</span>
      <span>FEDERAL WAY, WA 98117</span>
    </div>
    <div class="contact contact--phone">
      <span>BUSINESS PHONE (360)418-2096</span>
    </div>
    <div class="contact contact--fax">
      <span>FAX (360)418-2157</span>
      <span>OFFICE CELL PHONE (360)586-7319</span>
    </div>
    <div class="contact contact--email">
      <span>EMAIL</span>
    </div>
  </section>

  <section class="card card--back" aria-label="Back of card">
    <svg class="seal" width="200" height="200" viewBox="0 0 200 200" aria-hidden="true">
      <defs>
        <linearGradient id="ringGold" x1="0" y1="0" x2="1" y2="1">
          <stop offset="0" stop-color="#f6dc92"/>
          <stop offset=".5" stop-color="#e9ad3a"/>
          <stop offset="1" stop-color="#c98a1e"/>
        </linearGradient>
      </defs>
      <circle cx="100" cy="100" r="96" fill="none" stroke="#111216" stroke-width="4"/>
      <circle cx="100" cy="100" r="91" fill="none" stroke="url(#ringGold)" stroke-width="7"/>
      <circle cx="100" cy="100" r="86" fill="none" stroke="#15161a" stroke-width="2"/>
    </svg>

    <div class="band band--heading">
      <h2 class="section-title">OUR SPECIALIST</h2>
    </div>

    <ul class="services">
      <li class="service" style="top:374px">
        <svg class="service__arrow" viewBox="0 0 18 20" aria-hidden="true"><polygon points="0,0 18,10 0,20" fill="var(--gold)"/></svg>
        <span class="service__label">ACCOUNTING</span>
      </li>
      <li class="service" style="top:443px">
        <svg class="service__arrow" viewBox="0 0 18 20" aria-hidden="true"><polygon points="0,0 18,10 0,20" fill="var(--gold)"/></svg>
        <span class="service__label">PAYROLL</span>
      </li>
      <li class="service" style="top:511px">
        <svg class="service__arrow" viewBox="0 0 18 20" aria-hidden="true"><polygon points="0,0 18,10 0,20" fill="var(--gold)"/></svg>
        <span class="service__label">LICENSES</span>
      </li>
      <li class="service" style="top:578px">
        <svg class="service__arrow" viewBox="0 0 18 20" aria-hidden="true"><polygon points="0,0 18,10 0,20" fill="var(--gold)"/></svg>
        <span class="service__label">AUDITS</span>
      </li>
      <li class="service" style="top:633px">
        <svg class="service__arrow" viewBox="0 0 18 20" aria-hidden="true"><polygon points="0,0 18,10 0,20" fill="var(--gold)"/></svg>
        <span class="service__label">TAXES</span>
      </li>
    </ul>
    <span class="rule" style="top:418px"></span>
    <span class="rule" style="top:485px"></span>
    <span class="rule" style="top:556px"></span>
    <span class="rule" style="top:615px"></span>
    <span class="rule" style="top:667px"></span>

    <p class="firm-name">HALE ACCOUNTING</p>
  </section>

  <p class="card-label card-label--front">FRONT CARD</p>
  <p class="card-label card-label--back">BACK CARD</p>

</main>
</body>
</html>
```